Webdesign für ein Dachdeckerbetrieb
Zielgruppe
Wir sind ein Dachdeckerbetrieb.
Zielgruppe sind öffentliche Auftrageber , Hausverwaltungen und private Hausbesitzer.
Aufgabenstellung
Die Seite sollte übersichtlich sein. Nicht zuviele Menüs durch die man klicken muss.
Bilder können wir liefern .
Nach Vorgabe des Designers beschaffen wir die Bilder .
Logo ist vorhanden.

```html
<!DOCTYPE html>
<html lang="de">
<head>
<meta charset="utf-8">
<title>Brenner Dachbau – Dachdecker im Rhein-Main-Gebiet</title>
<link href="https://fonts.googleapis.com/css2?family=Heebo:wght@400;500;700&display=swap" rel="stylesheet">
<style>
:root{
  --green:#8cab22;
  --green-dark:#7b9a19;
  --dark:#393c3f;
  --text:#333537;
  --muted:#6d6f72;
  --grey-bg:#f1f1f1;
  --white:#ffffff;
}
*{box-sizing:border-box;margin:0;padding:0}
html,body{width:1200px;height:3056px;overflow:hidden}
body{font-family:"Heebo",Arial,sans-serif;color:var(--text);background:var(--white);position:relative}
.abs{position:absolute}
.section{position:absolute;left:0;width:1200px}
.tag{position:absolute;height:23px;padding:0 12px;font-size:13px;line-height:23px;color:var(--white);background:var(--green)}
.tag.dark{background:var(--dark)}
.btn{position:absolute;height:37px;background:var(--dark);color:var(--white);font-size:11px;font-weight:500;text-align:center;line-height:37px;border-radius:3px}
.accent{color:var(--green)}

/* header */
.site-header{top:0;height:71px;background:var(--white)}
.brand{position:absolute;left:235px;top:21px;display:flex;align-items:center;gap:8px;font-size:19px;font-weight:700;color:var(--green);letter-spacing:.5px}
.brand .mark{width:14px;height:14px;background:var(--green)}
.main-nav{position:absolute;left:456px;top:28px;display:flex;gap:27px;font-size:11px;color:var(--text)}
.main-nav .active{color:var(--green);font-weight:500}
.contact-btn{position:absolute;left:847px;top:19px;width:118px;height:30px;background:var(--dark);border-radius:2px;color:var(--white)}
.contact-btn svg{position:absolute;left:9px;top:7px}
.contact-btn .lbl{position:absolute;left:33px;top:3px;font-size:8px;color:var(--green)}
.contact-btn .num{position:absolute;left:33px;top:12px;font-size:11px}

/* hero */
.hero{top:71px;height:415px;background:linear-gradient(180deg,#3e7ab9 0%,#6a9ccc 28%,#a9c2d6 45%,#7c8b5a 60%,#8e8a6c 72%,#a6b04a 88%,#b8c241 100%)}
.hero-title{position:absolute;left:454px;top:72px;width:291px;height:42px;background:rgba(57,60,63,.75);color:var(--white);font-size:29px;font-weight:500;text-align:center;line-height:42px}
.hero-sub{position:absolute;left:0;width:1200px;text-align:center;color:var(--white);font-size:12.5px}

/* intro */
.intro{top:486px;height:539px}
.photo-top{left:235px;top:80px;width:293px;height:251px;border-radius:6px 6px 0 0;background:linear-gradient(160deg,#9cbde0 0%,#c9896a 35%,#a86e56 48%,#3b6ea3 70%,#2d5a8a 100%)}
.photo-small{left:235px;top:333px;width:122px;height:135px;border-radius:0 0 0 6px;background:linear-gradient(135deg,#b7b7b5,#7e7f80)}
.rating-box{left:359px;top:333px;width:169px;height:135px;background:var(--green);border-radius:0 0 6px 0;color:var(--white)}
.rating-box .score{position:absolute;left:21px;top:84px;font-size:14px;display:flex;gap:4px;align-items:center}
.rating-box .label{position:absolute;left:21px;top:104px;font-size:13px}
.intro h2{position:absolute;left:661px;top:113px;font-size:30px;font-weight:500;line-height:38px;color:var(--text)}
.intro p{position:absolute;left:662px;width:300px;font-size:11px;line-height:20px;color:var(--muted)}

/* services */
.services{top:1025px;height:869px;background:var(--grey-bg)}
.services h2{position:absolute;left:234px;top:96px;font-size:31px;font-weight:500}
.services .lead{position:absolute;left:235px;top:146px;width:730px;font-size:10.8px;line-height:20px;color:var(--muted)}
.card{position:absolute;width:231px;height:232px;overflow:hidden}
.card .shade{position:absolute;left:0;right:0;bottom:0;height:110px;background:linear-gradient(180deg,rgba(20,20,30,0),rgba(20,20,30,.75))}
.card span{position:absolute;left:24px;bottom:26px;color:var(--white);font-size:15px;font-weight:500}

/* stats */
.stats{top:1894px;height:114px;background:var(--green);color:var(--white)}
.stat{position:absolute;top:26px}
.stat svg{position:absolute;left:0;top:0}
.stat .n{position:absolute;left:42px;top:0;font-size:30px;font-weight:500;line-height:36px}
.stat .l{position:absolute;left:0;top:42px;font-size:13px;font-weight:500;white-space:nowrap}

/* arguments */
.arguments{top:2008px;height:560px;background:var(--grey-bg)}
.arguments h2{position:absolute;left:234px;top:118px;font-size:31px;font-weight:500;line-height:38px}
.arrow{position:absolute;top:142px;width:36px;height:36px;font-size:15px;text-align:center;line-height:36px;font-weight:700}
.slide{position:absolute;top:229px;width:357px;height:207px;border-radius:3px;overflow:hidden}
.slide .shade{position:absolute;left:0;right:0;bottom:0;height:100px;background:linear-gradient(180deg,rgba(30,20,15,0),rgba(30,20,15,.7))}
.slide .t{position:absolute;left:24px;bottom:34px;color:var(--white);font-size:15px;font-weight:500}
.slide .s{position:absolute;left:24px;bottom:20px;color:var(--white);font-size:10px}
.dots{position:absolute;left:572px;top:2491px;display:flex;gap:5px}
.dots i{display:block;width:11px;height:11px;border-radius:50%;border:1.5px solid #b9b9b9}
.dots i.on{border-color:var(--green)}

/* partners */
.partners{top:2568px;height:136px;background:var(--white)}
.partner{position:absolute;top:54px;width:76px;height:24px;background:#d7d7d7;border-radius:3px}

/* call band */
.callband{top:2704px;height:80px;background:var(--dark);color:var(--white)}
.callband .q{position:absolute;left:250px;top:27px;font-size:18px;font-weight:500}
.callband .q em{font-style:normal;font-weight:400;font-size:15px;color:var(--green)}
.callband .phone{position:absolute;left:721px;top:29px;font-size:15px;font-weight:700}
.callband svg{position:absolute;left:680px;top:24px}

/* footer */
.site-footer{top:2784px;height:272px;background:var(--green);color:var(--white)}
.site-footer h4{position:absolute;top:56px;font-size:12px;font-weight:500}
.site-footer ul{position:absolute;top:86px;list-style:none;font-size:10.5px}
.site-footer li{height:28px}
.site-footer li::before{content:"»";margin-right:7px}
.callback p{position:absolute;left:557px;top:86px;width:170px;font-size:10px;line-height:19px}
.field{position:absolute;left:557px;width:154px;height:24px;background:var(--white);color:#9a9a9a;font-size:8.5px;line-height:24px;padding-left:10px}
.send{position:absolute;left:557px;top:193px;width:80px;height:28px;border:1.5px solid var(--white);border-radius:2px;font-size:10px;font-weight:700;text-align:center;line-height:25px}
.foot-brand{position:absolute;left:781px;top:62px;display:flex;align-items:center;gap:7px;font-size:17px;font-weight:700;color:var(--white)}
.foot-brand .mark{width:12px;height:12px;background:var(--white)}
.contact{position:absolute;left:779px;font-size:10.5px;display:flex;align-items:center;gap:10px}
.social{position:absolute;top:203px;width:22px;height:22px;border:1.5px solid var(--white);border-radius:50%}
</style>
</head>
<body>

<header class="section site-header">
  <div class="brand"><span class="mark"></span>BRENNER DACHBAU</div>
  <nav class="main-nav">
    <span class="active">Startseite</span><span>Über uns</span><span>Referenzen</span><span>Leistungen</span><span>Kontakt</span>
  </nav>
  <div class="contact-btn">
    <svg width="16" height="16" viewBox="0 0 10 10" fill="none" stroke="#fff" stroke-width="1"><path d="M2 .5l2 2.5-1 1c.7 1.3 1.7 2.3 3 3l1-1 2.5 2-1 1.5C4 9 1 6 .5 1.5z"/></svg>
    <span class="lbl">Kontakt per Chat</span>
    <span class="num">0160-4827391</span>
  </div>
</header>

<section class="section hero" role="img" aria-label="Luftbild einer Ortschaft mit roten Dächern, Feldern und Windrädern unter blauem Himmel">
  <div class="hero-title">Für Sie <span class="accent">HOCH</span> hinaus</div>
  <div class="hero-sub" style="top:126px">Schön, Sie kennenzulernen!</div>
  <div class="hero-sub" style="top:145px">Ihr professioneller Dachdecker aus dem Rhein-Main Gebiet!</div>
</section>

<section class="section intro">
  <div class="abs photo-top" role="img" aria-label="Dach während der Neueindeckung mit Lattung und blauen Ziegeln"></div>
  <div class="abs photo-small" role="img" aria-label="Hammer und Arbeitshandschuhe auf Dachschindeln"></div>
  <div class="abs rating-box">
    <div class="score">4,8
      <svg width="62" height="11" viewBox="0 0 62 11" fill="#3d3f42"><g id="st"><polygon points="5.5,0 7,4 11,4 7.8,6.5 9,10.5 5.5,8 2,10.5 3.2,6.5 0,4 4,4"/></g><use href="#st" x="12.5"/><use href="#st" x="25"/><use href="#st" x="37.5"/><use href="#st" x="50"/></svg>
    </div>
    <div class="label">Kundenbewertungen</div>
  </div>
  <div class="tag" style="left:662px;top:81px">Solides Handwerk</div>
  <h2>Ist eine Sache,<br><span class="accent">Vertrauen</span> eine andere</h2>
  <p style="top:198px">Als Dachdecker-Meisterbetrieb sind wir der richtige Ansprechpartner für alle Arbeiten rund um ein fachgerechtes Dach, sowohl im privaten als auch im gewerblichen Bereich.</p>
  <p style="top:278px">Wir helfen Ihnen persönliche Wünsche mit technisch und fachlich richtigen Lösungen umzusetzen, egal ob Sie eine Neueindeckung oder eine Sanierung Ihres Wohnhauses wünschen, ob eine Wärmedämmung nach den neuesten gesetzlichen Vorgaben umgesetzt werden soll, ein Dachfenster eingebaut oder ersetzt werden soll oder eine Reparatur ansteht.</p>
  <div class="btn" style="left:662px;top:431px;width:136px">mehr erfahren</div>
</section>

<section class="section services">
  <div class="tag" style="left:235px;top:61px">Unser Leistungsspektrum</div>
  <h2>Aus Überzeugung!</h2>
  <p class="lead">Der Herausforderung ein Steildach, Ziegeldach oder Flachdach fachmännisch zu decken, stellen wir uns täglich gerne. Wir nehmen Ihre Wünsche in unserer anschließenden Planung auf und erarbeiten mit Ihnen und für Sie die optimale Lösung. Unser Leistungsspektrum beinhaltet selbstverständlich auch die Beseitigung und ordnungsgemäße Entsorgung von Asbest. Wir sorgen dafür, dass Sie ein solides und fachmännisch gewartetes Dach haben. Dafür stehen wir mit unserem Namen.</p>

  <div class="card" style="left:235px;top:252px;background:linear-gradient(150deg,#5b5e63,#2b2d31)" role="img" aria-label="Dunkle Dachziegel"><div class="shade"></div><span>Ziegeldach</span></div>
  <div class="card" style="left:485px;top:252px;background:linear-gradient(180deg,#4f86c6 0%,#9fbddb 45%,#8d8f94 60%,#5f6166 100%)" role="img" aria-label="Flachdach mit Lichtkuppeln"><div class="shade"></div><span>Flachdach</span></div>
  <div class="card" style="left:735px;top:252px;background:linear-gradient(180deg,#c9883f 0%,#d9d6cf 30%,#9ba087 65%,#6f7157 100%)" role="img" aria-label="Geöffnetes Dachflächenfenster mit Blick über eine Stadt"><div class="shade"></div><span>Dachflächenfenster</span></div>
  <div class="card" style="left:235px;top:503px;background:linear-gradient(150deg,#707070,#3f3f40)" role="img" aria-label="Hammer und Nägel auf Dachschindeln"><div class="shade"></div><span>Reparaturen &amp; Wartung</span></div>
  <div class="card" style="left:485px;top:503px;background:linear-gradient(160deg,#6b95d6 0%,#a4503a 35%,#b5b7ba 60%,#5a6fa6 100%)" role="img" aria-label="Dachrinne aus Metall unter roten Ziegeln"><div class="shade"></div><span>Bauklempnerei</span></div>
  <div class="card" style="left:735px;top:503px;background:linear-gradient(150deg,#4f9d8d 0%,#3f7c70 45%,#8d7c66 70%,#5d5248 100%)" role="img" aria-label="Trapezblech-Dach in Grün"><div class="shade"></div><span>Stehfalzarbeiten</span></div>

  <div class="btn" style="left:537px;top:768px;width:137px">mehr erfahren</div>
</section>

<section class="section stats">
  <div class="stat" style="left:259px">
    <svg width="34" height="32" viewBox="0 0 34 32" fill="none" stroke="#fff" stroke-width="1.6"><path d="M17 2L2 28h30z"/><path d="M8 18h18M11 12h12M17 2v26"/></svg>
    <span class="n">213</span><span class="l">fertiggestellte Projekte</span>
  </div>
  <div class="stat" style="left:457px">
    <svg width="36" height="32" viewBox="0 0 36 32" fill="none" stroke="#fff" stroke-width="1.6"><circle cx="18" cy="7" r="4"/><circle cx="8" cy="18" r="3.5"/><circle cx="28" cy="18" r="3.5"/><path d="M2 30c0-5 3-7 6-7s6 2 6 7M22 30c0-5 3-7 6-7s6 2 6 7M12 22c0-5 3-8 6-8s6 3 6 8"/></svg>
    <span class="n">306</span><span class="l">zufriedene Kunden</span>
  </div>
  <div class="stat" style="left:634px">
    <svg width="32" height="32" viewBox="0 0 32 32" fill="none" stroke="#fff" stroke-width="1.6"><path d="M8 12a8 8 0 0116 0z"/><path d="M6 12h20"/><circle cx="16" cy="17" r="4"/><path d="M4 31c0-6 5-9 12-9s12 3 12 9z"/></svg>
    <span class="n">22</span><span class="l">motivierte Angestellte</span>
  </div>
  <div class="stat" style="left:816px">
    <svg width="30" height="34" viewBox="0 0 30 34" fill="none" stroke="#fff" stroke-width="1.6"><circle cx="15" cy="12" r="10"/><circle cx="15" cy="12" r="5"/><path d="M9 20l-3 12 5-3 3 4 1-9M21 20l3 12-5-3-3 4"/></svg>
    <span class="n">100%</span><span class="l">professionelle Arbeit</span>
  </div>
</section>

<section class="section arguments">
  <div class="tag dark" style="left:235px;top:82px">Unsere Argumente</div>
  <h2>Unser <span class="accent">Handwerk</span>,<br>das sich <span class="accent">zeigen</span> lässt</h2>
  <div class="arrow" style="left:885px;background:var(--white);color:var(--green)">«</div>
  <div class="arrow" style="left:929px;background:#8b9098;color:var(--white)">»</div>
  <div class="slide" style="left:235px;background:linear-gradient(160deg,#9b6a4e,#6e7b47 45%,#7a4c39)" role="img" aria-label="Bemooste, beschädigte Dachziegel"><div class="shade"></div><span class="t">Durch Alterung beschädigtes Dach</span><span class="s">Vorher</span></div>
  <div class="slide" style="left:610px;background:linear-gradient(160deg,#c25a35,#a5452a 50%,#7b3420)" role="img" aria-label="Neu eingedecktes rotes Ziegeldach mit Dachfenster"><div class="shade"></div><span class="t">Durch uns fachmännisch erneuert</span><span class="s">Nachher</span></div>
</section>
<div class="dots"><i class="on"></i><i></i><i></i><i></i></div>

<section class="section partners">
  <div class="partner" style="left:252px"></div>
  <div class="partner" style="left:420px"></div>
  <div class="partner" style="left:570px"></div>
  <div class="partner" style="left:726px"></div>
  <div class="partner" style="left:884px"></div>
</section>

<section class="section callband">
  <div class="q">Haben Sie weitere Fragen? <em>Wir haben die Antworten!</em></div>
  <svg width="30" height="30" viewBox="0 0 30 30" fill="none" stroke="#8cab22" stroke-width="1.8"><path d="M6 3l5 6-3 3c2 4 5 7 9 9l3-3 6 5-3 4C12 27 3 18 2 7z"/><path d="M17 5a9 9 0 018 8M17 10a4 4 0 013 3"/></svg>
  <div class="phone">von 8-17 Uhr: 0 61 45 - 72 41 58</div>
</section>

<footer class="section site-footer">
  <h4 style="left:250px">Navigation</h4>
  <ul style="left:250px"><li>Startseite</li><li>Über uns</li><li>Referenzen</li><li>Leistungen</li><li>Kontakt</li></ul>
  <h4 style="left:398px">Rechtliches</h4>
  <ul style="left:398px"><li>Datenschutz</li><li>AGB</li><li>Impressum</li></ul>
  <h4 style="left:557px">Rückrufservice</h4>
  <div class="callback"><p>Wir rufen Sie schnellst möglich an und helfen Ihnen weiter!</p></div>
  <div class="field" style="top:130px">Ihr Name</div>
  <div class="field" style="top:159px">Telefonnummer</div>
  <div class="send">absenden</div>

  <div class="foot-brand"><span class="mark"></span>BRENNER DACHBAU</div>
  <div class="contact" style="top:118px"><svg width="9" height="11" viewBox="0 0 9 11" fill="none" stroke="#fff"><path d="M4.5 10.5S1 6.5 1 4a3.5 3.5 0 017 0c0 2.5-3.5 6.5-3.5 6.5z"/><circle cx="4.5" cy="4" r="1.2"/></svg>Lindenweg 12, 55411 Tannhausen</div>
  <div class="contact" style="top:138px"><svg width="10" height="9" viewBox="0 0 10 9" fill="none" stroke="#fff"><rect x=".5" y=".5" width="9" height="8"/><path d="M.5 .5l4.5 4 4.5-4"/></svg>info@brenner-dachbau.example</div>
  <div class="contact" style="top:158px"><svg width="10" height="10" viewBox="0 0 10 10" fill="none" stroke="#fff"><path d="M2 .5l2 2.5-1 1c.7 1.3 1.7 2.3 3 3l1-1 2.5 2-1 1.5C4 9 1 6 .5 1.5z"/></svg>06145 - 72 41 58</div>
  <div class="social" style="left:778px"></div>
  <div class="social" style="left:804px"></div>
  <div class="social" style="left:830px"></div>
</footer>

</body>
</html>
```